Flyer Design Project

opening a preschool and need to hand out flyers to advertise at an expo on Feb.1st. It is geared toward 3-4 year old potty trained children. I have more that 10+ years teaching experience and it will be a private preschool with small class sizes and individual instruction and attention. You can look at the website, it is www.brightmaplekids.net. I tried to make a flyer but I can't make it with high enough resolution. I attached the logo and my attempted flyer.

Industry/Entity Type

Preschool

```html
<!DOCTYPE html>
<html lang="en">
<head>
<meta charset="utf-8">
<title>Bright Maple Kids – Early Bird Special</title>
<link href="https://fonts.googleapis.com/css2?family=Chango&family=Open+Sans:wght@400;600&display=swap" rel="stylesheet">
<style>
  :root{
    --teal:#2ba3a3;
    --teal-dark:#23898a;
    --pink:#c5569c;
    --green:#a8c31b;
    --orange:#f07a22;
    --ink:#2b2b2b;
    --paper:#fbfcfd;
    --grid:#c9dcec;
    --white:#ffffff;
  }
  html,body{margin:0;padding:0;overflow:hidden;}
  body{background:#fff;}
  .flyer{
    position:relative;width:784px;height:1200px;overflow:hidden;
    background:var(--teal);
    font-family:"Open Sans",Arial,sans-serif;color:var(--ink);
  }
  .sheet{
    position:absolute;background-color:var(--paper);
    background-image:
      linear-gradient(var(--grid) 1px,transparent 1px),
      linear-gradient(90deg,var(--grid) 1px,transparent 1px);
    background-size:15px 15px;
    box-shadow:0 4px 12px rgba(0,0,0,.25);
  }
  .sheet--top{left:29px;top:60px;width:638px;height:505px;}
  .sheet--bottom{left:193px;top:556px;width:572px;height:614px;transform:rotate(0.4deg);}
  .holes{position:absolute;left:-10px;top:0;}
  .ruler{position:absolute;left:26px;top:572px;width:120px;height:560px;
    background:linear-gradient(90deg,#f7922e,#e8711b);transform:rotate(-24deg);transform-origin:top left;}
  .deco-letter{position:absolute;border-radius:24px;}
  .deco-letter--b{left:618px;top:150px;width:140px;height:152px;background:var(--green);}
  .deco-letter--e{left:30px;top:935px;width:118px;height:135px;background:var(--pink);}
  .pin{position:absolute;width:34px;height:34px;border-radius:50%;}
  .pin--yellow{left:70px;top:50px;background:#f4c21c;}
  .pin--pink{left:730px;top:538px;background:#e98dbb;}
  .t{position:absolute;margin:0;white-space:nowrap;}
  .headline{left:160px;top:86px;font-family:"Chango",Georgia,serif;font-size:35px;}
  .headline .a{color:var(--pink)}.headline .b{color:var(--green)}.headline .c{color:var(--orange)}
  .enroll{left:116px;top:140px;font-size:16.5px;text-decoration:underline;}
  .intro{left:181px;top:194px;font-size:23px;}
  .centre-name{left:181px;top:226px;font-size:31px;}
  .offer-label{left:116px;top:292px;font-size:34px;color:var(--teal);}
  .offer-days{left:320px;top:305px;font-size:19px;}
  .offer-line{left:117px;font-size:22.5px;}
  .offer-line--small{font-size:19.5px;}
  .safe{left:116px;top:478px;font-size:28.5px;}
  .about-title{left:331px;top:583px;font-size:33px;color:var(--teal);}
  .about{left:268px;top:676px;width:500px;font-size:20.5px;line-height:29px;white-space:normal;margin:0;position:absolute;}
  .teacher{left:260px;top:825px;width:494px;font-size:23px;line-height:34px;color:var(--orange);text-align:justify;text-align-last:justify;position:absolute;margin:0;}
  .about--2{left:270px;top:895px;}
  .call{left:321px;top:1009px;font-size:13px;}
  .contact{left:313px;top:1018px;font-size:34px;}
  .contact .lbl{color:var(--green)}.contact .num{color:var(--pink)}
  .link{left:318px;font-size:17px;text-decoration:underline;color:var(--ink);}
  .addr{left:321px;top:1106px;font-size:17px;}
  .footnote{left:23px;top:1163px;font-size:20px;color:var(--white);}
</style>
</head>
<body>
<main class="flyer">
  <section class="sheet sheet--top">
    <svg class="holes" width="90" height="505" viewBox="0 0 90 505" aria-hidden="true">
      <g fill="var(--teal)">
        <circle cx="50" cy="60" r="21"/><circle cx="50" cy="133" r="21"/><circle cx="50" cy="207" r="21"/>
        <circle cx="50" cy="282" r="21"/><circle cx="50" cy="356" r="21"/><circle cx="50" cy="429" r="21"/>
        <circle cx="50" cy="498" r="21"/>
      </g>
    </svg>
  </section>
  <div class="deco-letter deco-letter--b" role="img" aria-label="Large decorative green letter B"></div>
  <div class="pin pin--yellow" role="img" aria-label="Yellow push pin"></div>

  <h1 class="t headline"><span class="a">Early</span> <span class="b">Bird</span> <span class="c">Special!</span></h1>
  <p class="t enroll">Enroll before March 31st,2016 &amp; have your application fee waived.</p>
  <p class="t intro">Students will love learning @</p>
  <p class="t centre-name">Bright Maple Kids!</p>
  <h2 class="t offer-label">WE OFFER :</h2>
  <p class="t offer-days">Monday through Friday classes</p>
  <p class="t offer-line" style="top:332px">Competitive rates with high quality education,</p>
  <p class="t offer-line" style="top:364px">small classes, allowing for individual attention.</p>
  <p class="t offer-line offer-line--small" style="top:403px">Lots of creativity, discovery and learning through play.</p>
  <p class="t safe">A safe, happy &amp;fun-filled environment</p>

  <div class="ruler" role="img" aria-label="Orange ruler"></div>

  <section class="sheet sheet--bottom">
    <svg class="holes" width="90" height="614" viewBox="0 0 90 614" aria-hidden="true">
      <g fill="#b55d16">
        <circle cx="50" cy="60" r="19" fill="#bbbbbb"/><circle cx="50" cy="120" r="19"/><circle cx="50" cy="180" r="19"/>
        <circle cx="50" cy="240" r="19"/><circle cx="50" cy="306" r="19"/><circle cx="50" cy="372" r="19"/>
        <circle cx="50" cy="434" r="19"/><circle cx="50" cy="496" r="19" fill="var(--teal-dark)"/><circle cx="50" cy="560" r="19" fill="var(--teal)"/>
      </g>
    </svg>
  </section>
  <div class="pin pin--pink" role="img" aria-label="Pink push pin"></div>
  <div class="deco-letter deco-letter--e" role="img" aria-label="Large decorative pink letter E"></div>

  <h2 class="t about-title">WHAT WE ARE ABOUT :</h2>
  <p class="about">Bright Maple Kids is a private preschool geared towards potty- trained children ages 3-4 years old. With a specialized curriculum, you can be assured that your child will be prepared when entering the world of education,</p>
  <p class="teacher">Mrs. Harlow is a licensed teacher with 10+ years of Elementary School experience.</p>
  <p class="about about--2">She knows what your child needs to be prepared for the rigour of K-12 education, and how to build that foundation for the future.</p>

  <p class="t call">Please call for more information on schedules.</p>
  <p class="t contact"><span class="lbl">Contact us @</span> <span class="num">555-014-2738</span></p>
  <p class="t link" style="top:1057px">www.brightmaplekids.net</p>
  <p class="t link" style="top:1081px">jenharlow@brightmaplekids.net</p>
  <p class="t addr">#4180 Linden Way Fairview, CO 80000</p>

  <p class="t footnote">You must be accepted &amp; enrolled for application fee to be waived.</p>
</main>
</body>
</html>
```